The Ballad of Orlena

I need a design for a two-page spread to open a very long (and fascinating) story about a famous female architect who basically built our very charming village. I've enclosed copy, photo of her, and several images of key buildings.

My present concept (I'm very open to other ideas) is a female hand with a drafting pencil, working on a blue line, with our town's iconic buildings designed by Orlena Pratt, Ojai, California, gradually coming into view toward the bottom of the page.

The first paragraph of copy (above the byline) should go on the first left-hand page, then the 7,500 story should follow on the right-hand side. But again, just a suggestion.

Our quarterly magazine is universally regarded as having superior, long-form journalism (the Harbor Quill of California, as someo, but our design execution is weak. We need your help.

Target Market(s)

Ojai is an affluent, highly artistic community. And our magazine is expanding nationwide to appeal to both tourists and the rising creative class of people who would be drawn to a community like Ojai.

Industry/Entity Type

Architect

Requirements
Must have
• Page specs …

8.375" by 10.875" trim
8.875" by 11.375" bleed (.25" all around)
Spread 17.25" by 11.375" bleed.

Copy …
We use Neutra for headlines and cutlines, Berkeley OldStyle for copy, subheads. But I like the idea of using Glimmerset - the old Quest of Morvane typeface for the main headline.

```html
<!DOCTYPE html>
<html lang="en">
<head>
<meta charset="utf-8">
<title>The Ballad of Orlena</title>
<link rel="stylesheet" href="https://fonts.googleapis.com/css2?family=Jost:wght@300;400;600;700&family=Sorts+Mill+Goudy&display=swap">
<style>
  :root {
    --paper: #ffffff;
    --ink: #111111;
    --portrait-tone-a: #d8d6d2;
    --portrait-tone-b: #6e6b66;
    --sky: #3a78d6;
    --stucco: #e9e4da;
    --garden-a: #6d7f5a;
    --garden-b: #c9b58a;
  }
  * { margin: 0; padding: 0; box-sizing: border-box; }
  html, body { width: 1200px; height: 779px; overflow: hidden; background: var(--paper); }
  .spread { position: relative; width: 1200px; height: 779px; background: var(--paper); color: var(--ink); overflow: hidden; }

  .headline { position: absolute; left: 0; top: 0; width: 1200px; height: 260px; }
  .headline text { font-family: "Jost", sans-serif; font-weight: 600; fill: var(--ink); }

  .intro { position: absolute; left: 227px; top: 299px; width: 345px;
    font-family: "Jost", sans-serif; font-weight: 300; font-size: 12.9px; line-height: 17.4px; }
  .byline { position: absolute; left: 227px; top: 431px; font-family: "Jost", sans-serif;
    font-size: 7.4px; line-height: 10px; text-transform: uppercase; letter-spacing: .02em; }
  .byline strong { font-weight: 700; display: block; }

  .photo { position: absolute; }
  .photo-house { left: 30px; top: 480px; width: 180px; height: 137px;
    background: linear-gradient(180deg, #9aa9c4 0%, var(--garden-b) 55%, var(--garden-a) 100%); }
  .photo-portrait { left: 226px; top: 478px; width: 349px; height: 301px;
    background: radial-gradient(ellipse at 45% 45%, var(--portrait-tone-a) 0%, #a9a6a1 55%, var(--portrait-tone-b) 100%); }
  .photo-arcade { left: 632px; top: 303px; width: 360px; height: 176px;
    background: linear-gradient(180deg, var(--sky) 0%, #7fa6de 38%, var(--stucco) 52%, #b9b1a3 78%, #7a7670 100%); }

  .column { position: absolute; width: 176px; overflow: hidden;
    font-family: "Sorts Mill Goudy", serif; font-size: 9.3px; line-height: 11.1px; }
  .column p + p { margin-top: 11px; }
  .col-one { left: 632px; top: 495px; height: 284px; }
  .col-two { left: 817px; top: 495px; height: 284px; }
  .col-three { left: 1004px; top: 303px; width: 178px; height: 476px; }
  .lede { font-weight: 700; -webkit-text-stroke: .35px var(--ink); }
</style>
</head>
<body>
<main class="spread">
  <svg class="headline" viewBox="0 0 1200 260" aria-label="Orlena">
    <text x="0" y="254" font-size="346" textLength="1200" lengthAdjust="spacingAndGlyphs">ORLENA</text>
  </svg>

  <p class="intro">Ojai didn’t take its present form through gradual changes. Instead, it was through several phases of what biologists call “punctuated equilibrium.” First, the fire of 1916 left a clean slate for Edwin Harlow Marsh and his merry band of civic pioneers and philanthropists. Then, the Hollywood Blacklist brought Ojai another. Her name was Orlena Pratt. This is her story.</p>

  <p class="byline"><strong>Orlena’s World</strong>By Lorraine Whitfield Haskell</p>

  <div class="photo photo-house" role="img" aria-label="Photograph of a modern house designed by Orlena Pratt, lit at dusk among trees"></div>
  <div class="photo photo-portrait" role="img" aria-label="Black and white portrait photograph of the architect Orlena Pratt before bookshelves"></div>
  <div class="photo photo-arcade" role="img" aria-label="Photograph of the white arched arcade along Ojai’s main street with mountains and blue sky behind"></div>

  <article class="column col-one">
    <p class="lede">Few individuals have left so many indelible marks on the Ojai area landscape as architect Orlena Pratt, a supreme talent, a great wit and a dear friend. She and I became acquainted through our mutual support of Ventura County Supervisor Margit Ellison Tarn. Orlena, “citizen warrior” Celia Brant, Doris Kellner — county Counsel for Ventura County, the first woman in the state to hold such a position — and I would travel from Ojai to wherever the “Friends of Margit” were meeting and, in the process, became great friends.</p>
    <p>Before long, we became “Ladies Who Lunch,” whenever we could work it into our schedules. It was in 1993, when Orlena, Vice President (Vice Chair? Don’t think the board has VP, but you’d know better than I) of the Valley Landmarks Review Board, suggested I join her on the board — not because I knew anything</p>
  </article>

  <article class="column col-two">
    <p>about history, preservation, or city law, but because she said she would have much more fun with me on board. Now, for the rest of her story.</p>
    <p>Orlena’s creations in Ojai are lived in, learned in, worked in, prayed in and crossed over. But I didn’t realize how little I knew about Orlena until after her death in 1996, when I was asked to give a talk about her life; research led me to discover her roots, her childhood, her marriage to the equally talented Martin Pratt — and her fabulous career.</p>
    <p>Consider, for example, the story of her parents and the precarious life they lived in Lithuania and Belarus. Simna, Lithuania, the home of Orlena’s mother, Hanna Feldberg, was about two hours out of Vilnius — since the 14th century, the center of Jewish culture and learning. But by the time of Hanna’s birth in 1892, Lithuanians had been forbidden to speak their own</p>
  </article>

  <article class="column col-three">
    <p>language and Jews were forbidden to own land, reduced to living in ghettos and subject to periodic pogroms of Czarist Russia. Hanna, orphaned at an early age, was living with her Tante Dora.</p>
    <p>About 200 miles away, in Belarus, the same sort of persecution was underway, a period of intense “Russification.” Orlena’s father, Aron Lisker, who was living with his widowed mother and apprenticed to a hat-maker, was stopped by the police on one of his deliveries. A note was discovered in the hat: “Come to meeting tonight.” With that startling discovery, as well as the threat of enforced service in the Czar’s Army, Aron and his mother decided it was time for him to leave for the land of opportunity. He was 16 years of age.</p>
    <p>On the way, he and a cousin stopped in to visit friends and relatives in Simna. Hanna was entranced. Many years later, she would relate: “I thought he was the smartest and loveliest looking person I’d ever seen.” But, at 11 years of age, she was far too young to think of joining him on his adventure, said Tante Dora.</p>
    <p>But just one-and-a-half years later, bearing a goose-down quilt, a long bread and long salami as dowry, 12-almost-13-years-old Hanna set out for New York City to join relatives who had emigrated earlier. After her arrival, she was cautioned by Tante Mirel, “You cannot go chasing after a boy without observing the proprieties; you simply must have a hat.”</p>
    <p>So Hanna submitted an ad to the Manhattan Ledger: “Excellent seamstress recently arrived NYC. Wishes employment.” In</p>
  </article>
</main>
</body>
</html>
```